Elegant Black Candle Label Design!

I need a 2.375" tall by 3.0" wide candle label design. I'm looking for simple and elegant. Black label with silver leaf border and lettering. Label needs to have the following information on it: Fern Hollow Candle Co. as the company name, scent name in the middle and in smaller font, it needs to say Made in USA, All Natural, 8oz. Attached photos are for inspiration.

Target Market(s)

People looking for high end, all natural candle fragrances

Industry/Entity Type

Candle-Spa

Colors

Designer to choose only greyscale colors for use in the design.

Requirements
Must have
• Company Name, Scent (ability to change scent names), All Natural, Made in USA, 8oz
Nice to have
• Black background, silver leaf border and silver leaf font. Elegant fonts maybe slightly cursive

```html
<!DOCTYPE html>
<html lang="en">
<head>
<meta charset="UTF-8">
<title>Fern Hollow Candle Co. — Label</title>
<link href="https://fonts.googleapis.com/css2?family=Josefin+Sans:wght@300;400&display=swap" rel="stylesheet">
<style>
  :root {
    --backdrop: #e4e4e4;
    --label-black: #0d0d0d;
    --leaf-band: #222222;
    --leaf-edge: #363636;
    --silver: #c9c9c9;
    --silver-soft: #a8a8a8;
  }
  * { margin: 0; padding: 0; box-sizing: border-box; }
  html, body {
    width: 1200px;
    height: 994px;
    overflow: hidden;
    background: var(--backdrop);
  }
  .canvas {
    position: relative;
    width: 1200px;
    height: 994px;
  }
  .label {
    position: absolute;
    left: 50px;
    top: 62px;
    width: 1100px;
    height: 870px;
    background: var(--label-black);
  }
  .leaf-border {
    position: absolute;
    inset: 22px;
    border: 40px solid var(--leaf-band);
    box-shadow: inset 0 0 0 2px var(--leaf-edge), 0 0 0 2px var(--leaf-edge);
  }
  .frame-line {
    position: absolute;
    inset: 58px;
    border: 2px solid var(--silver-soft);
    border-radius: 22px;
  }
  .content {
    position: absolute;
    inset: 58px;
    text-align: center;
    color: var(--silver);
    font-family: "Josefin Sans", sans-serif;
  }
  .brand {
    position: absolute;
    top: 150px;
    left: 0;
    right: 0;
    font-weight: 300;
    font-size: 62px;
    line-height: 1.1;
    letter-spacing: 2px;
    color: var(--silver);
  }
  .brand-sub {
    display: block;
    font-size: 28px;
    letter-spacing: 6px;
    margin-top: 12px;
    text-transform: uppercase;
  }
  .scent {
    position: absolute;
    top: 420px;
    left: 0;
    right: 0;
    font-weight: 300;
    font-size: 36px;
    letter-spacing: 14px;
  }
  .divider {
    position: absolute;
    top: 538px;
    left: 50%;
    width: 140px;
    margin-left: -70px;
    height: 2px;
    background: var(--silver-soft);
  }
  .details {
    position: absolute;
    top: 612px;
    left: 0;
    right: 0;
    font-weight: 300;
    font-size: 27px;
    line-height: 1.8;
    letter-spacing: 1px;
  }
</style>
</head>
<body>
  <div class="canvas">
    <section class="label">
      <div class="leaf-border"></div>
      <div class="frame-line"></div>
      <div class="content">
        <h1 class="brand">Fern Hollow<span class="brand-sub">Candle Co.</span></h1>
        <h2 class="scent">MIDNIGHT AMBER</h2>
        <div class="divider"></div>
        <p class="details">Made in USA | All Natural<br>8oz</p>
      </div>
    </section>
  </div>
</body>
</html>
```